Werbesprüche und/oder Design für Schmutzschleusen
Zielgruppe
Die KLV GmbH ist als Schienenpersonennahverkehrsunternehmen grenzüberschreitend zwischen der Schweiz und Deutschland unterwegs.
Unsere Züge sollen nun in den Eingangsbereichen mit Teppichen (Schmutzschleusen) ausgestattet werden.
Die Zielgruppe sind unsere Fahrgäste; also Pendler, Studenten, Schüler, Touristen etc...
Aufgabenstellung
Der Teppich ist 142 x 262 cm groß. Die schmalen Seiten liegen jeweils an den Ein- und Ausstiegen.
Der Großteil des Teppichs soll recht dunkel gehalten werden, so dass Schmutzablagerungen nicht gleich ersichtlich sind: d.h. dunkelgrau, dunkelrot, dunkelblau, dunkelgrün etc....
Da einfarbig monoton wirkt, beabsichtigen wir einen kreativen Spruch/Grafik/Piktogramm etc. zu integrieren, welche/s sich vom Hintergrund farblich abhebt.
Die Fahrgäste sollen mit einem Schmunzeln in den Zug einsteigen bzw. sich wohlfühlen.
Der Spruch und/oder die Grafik sollen von beiden Einstiegsseiten (schmale Seite mit 142 cm) gut gelesen werden können.
Unsere Logos können, müssen aber nicht verwendet werden.
Da wir in verschiedenen Regionen unterwegs sind, bitte entweder das KLV-Logo alleinig verwenden oder in folgenden Kombinationen: KLV + moorfink-Logo oder KLV + Talbahn-Logo.

```html
<!DOCTYPE html>
<html lang="de">
<head>
<meta charset="utf-8">
<title>KLV Schmutzschleuse – An mir!</title>
<link rel="stylesheet" href="https://fonts.googleapis.com/css2?family=Cabin:wght@700&display=swap">
<style>
  :root {
    --mat-green: #022c06;
    --signal-green: #46f00a;
    --brand-red: #ff0000;
    --logo-white: #ffffff;
  }
  html, body {
    margin: 0;
    padding: 0;
    width: 1200px;
    height: 2214px;
    overflow: hidden;
    background: var(--mat-green);
  }
  .mat {
    position: relative;
    width: 1200px;
    height: 2214px;
    background: var(--mat-green);
    font-family: "Cabin", "Gill Sans", sans-serif;
    font-weight: 700;
  }
  .entry-side {
    position: absolute;
    left: 0;
    width: 1200px;
    height: 1107px;
  }
  .entry-side--near { top: 1107px; }
  .entry-side--far { top: 0; transform: rotate(180deg); }
  .entry-side svg { display: block; width: 1200px; height: 1107px; }
  .slogan { fill: var(--signal-green); font-family: inherit; font-weight: 700; }
  .slogan--question { font-size: 86px; }
  .slogan--answer { font-size: 235px; }
  .brand-mark { fill: var(--brand-red); }
  .brand-name { fill: var(--logo-white); font-family: inherit; font-weight: 700; font-size: 52px; }
  .brand-name--line { letter-spacing: 4px; }
</style>
</head>
<body>
<main class="mat">
  <section class="entry-side entry-side--far" aria-label="Spruch für die gegenüberliegende Tür">
    <svg viewBox="0 0 1200 1107" xmlns="http://www.w3.org/2000/svg">
      <text class="slogan slogan--question" x="86" y="591" textLength="941" lengthAdjust="spacingAndGlyphs">… und an wem bleibt´s</text>
      <text class="slogan slogan--question" x="1109" y="690" text-anchor="end">wieder hängen?</text>
      <text class="slogan slogan--answer" x="308" y="870" textLength="569" lengthAdjust="spacingAndGlyphs">An mir!</text>
      <rect class="brand-mark" x="236" y="1012" width="43" height="43"/>
      <text class="brand-name" x="294" y="1052">KLV</text>
      <text class="brand-name brand-name--line" x="709" y="1052">Talbahn</text>
    </svg>
  </section>
  <section class="entry-side entry-side--near" aria-label="Spruch für diese Tür">
    <svg viewBox="0 0 1200 1107" xmlns="http://www.w3.org/2000/svg">
      <text class="slogan slogan--question" x="86" y="591" textLength="941" lengthAdjust="spacingAndGlyphs">… und an wem bleibt´s</text>
      <text class="slogan slogan--question" x="1109" y="690" text-anchor="end">wieder hängen?</text>
      <text class="slogan slogan--answer" x="308" y="870" textLength="569" lengthAdjust="spacingAndGlyphs">An mir!</text>
      <rect class="brand-mark" x="236" y="1012" width="43" height="43"/>
      <text class="brand-name" x="294" y="1052">KLV</text>
      <text class="brand-name brand-name--line" x="709" y="1052">Talbahn</text>
    </svg>
  </section>
</main>
</body>
</html>
```